dessert restaurant

I need a business card design for my restaurant. It will primarily be a dessert and wine restaurant. I will serve delicious baked from scratch desserts, cake, pies cookies brownies etc. Select red and white wines.I will also offer light breakfast, and lunch menu. This will be an upscale contemporary design restaurant with reasonably priced items on the menu. I will also offer small plates in the evening with dessert menu. my color scheme is cobalt blue , red, white black. My restaurant will be the place where adults come after enjoying the meal at a restaurant and want to enjoy a dessert and a glass of wine to finish off their evening. I will also have contemporary jazz sounds for atmosphere.

Industry/Entity Type

Restaurant

Contact Information for Business Card

tessa marlowe 415 555 0193

```html
<!DOCTYPE html>
<html lang="en">
<head>
<meta charset="utf-8">
<title>Velvet Crumb – Business Card</title>
<link rel="stylesheet" href="https://fonts.googleapis.com/css2?family=Open+Sans:wght@400;600;700&display=swap">
<style>
  :root {
    --backdrop: #e4e1dc;
    --card: #f7f6f3;
    --ink: #2a2623;
    --panel: #0b0b0b;
    --wine-red: #c8202f;
  }
  * { margin: 0; padding: 0; box-sizing: border-box; }
  html, body {
    width: 1200px;
    height: 800px;
    overflow: hidden;
    background: var(--backdrop);
  }
  .canvas {
    position: relative;
    width: 1200px;
    height: 800px;
  }
  .business-card {
    position: absolute;
    left: 162px;
    top: 150px;
    width: 876px;
    height: 500px;
    background: var(--card);
    box-shadow: 0 10px 30px rgba(0,0,0,0.18);
    font-family: "Open Sans", sans-serif;
    overflow: hidden;
  }
  .brand {
    position: absolute;
    left: 90px;
    top: 245px;
    display: flex;
    align-items: center;
    gap: 16px;
  }
  .brand-dot {
    width: 22px;
    height: 22px;
    border-radius: 50%;
    background: var(--wine-red);
  }
  .brand-name {
    font-size: 42px;
    font-weight: 600;
    color: var(--ink);
    letter-spacing: 1px;
  }
  .contact-panel {
    position: absolute;
    left: 455px;
    top: 90px;
    right: 0;
    height: 262px;
    background: var(--panel);
    border-radius: 36px 0 0 36px;
    padding: 62px 0 0 70px;
    color: var(--wine-red);
  }
  .contact-name {
    font-size: 34px;
    font-weight: 700;
    line-height: 1.1;
  }
  .contact-role {
    font-size: 22px;
    font-weight: 400;
    margin-top: 10px;
  }
  .contact-phone {
    display: flex;
    align-items: center;
    gap: 12px;
    font-size: 30px;
    font-weight: 400;
    letter-spacing: 1px;
    margin-top: 14px;
  }
  .phone-icon { width: 26px; height: 26px; }
  .address {
    position: absolute;
    left: 0;
    right: 0;
    bottom: 46px;
    text-align: center;
    font-size: 22px;
    letter-spacing: 2.5px;
    color: var(--ink);
  }
</style>
</head>
<body>
<main class="canvas">
  <section class="business-card">
    <div class="brand">
      <span class="brand-dot"></span>
      <span class="brand-name">Velvet Crumb</span>
    </div>

    <div class="contact-panel">
      <p class="contact-name">Tessa Marlowe</p>
      <p class="contact-role">Director</p>
      <p class="contact-phone">
        <svg class="phone-icon" viewBox="0 0 24 24" aria-hidden="true">
          <path fill="currentColor" d="M6.6 10.8a15.1 15.1 0 0 0 6.6 6.6l2.2-2.2a1 1 0 0 1 1-.25 11.4 11.4 0 0 0 3.6.57 1 1 0 0 1 1 1V20a1 1 0 0 1-1 1A17 17 0 0 1 3 4a1 1 0 0 1 1-1h3.5a1 1 0 0 1 1 1c0 1.25.2 2.45.57 3.57a1 1 0 0 1-.25 1z"/>
        </svg>
        <span>415 555 0193</span>
      </p>
    </div>

    <p class="address">418 Harlow St. N.W. Wash. D.C. 20009</p>
  </section>
</main>
</body>
</html>
```